Bramble Ridge Club TRAINING CAMP

I need one flyer for two training camps that will be held in Tuscany (Italy) next October and Novembre 2015
My company: www.brambleridgeclub.example uses mainly black, read and white colours. Attached in the files is also a template i like and that i would like to use.
I

Target Market(s)

competitive cyclists

Industry/Entity Type

It Company

Font styles to use
Sans Serif
Other font styles liked:
• Arial

Colors
ec1f27
ffffff
000000
9d9d9d
cbcbcb

Requirements
Must have
• English version and Italian version. I will provide both translations
Nice to have
• 2 pages or 3 pages in half A4 international size
• first one with camp general overview
• second one with description of the contents and coaches

```html
<!DOCTYPE html>
<html lang="en">
<head>
<meta charset="utf-8">
<title>Bramble Ridge Club – Tuscany Training Camps</title>
<link rel="stylesheet" href="https://fonts.googleapis.com/css2?family=Oswald:wght@500;700&family=Arimo:wght@400;700&display=swap">
<style>
  :root {
    --red: #ec1f27;
    --white: #ffffff;
    --black: #000000;
    --grey: #9d9d9d;
    --light-grey: #cbcbcb;
  }
  * { margin: 0; padding: 0; box-sizing: border-box; }
  html, body { width: 849px; height: 1200px; overflow: hidden; background: var(--black); }
  .flyer {
    position: relative;
    width: 849px;
    height: 1200px;
    overflow: hidden;
    background: var(--black);
    font-family: "Arimo", Arial, sans-serif;
    color: var(--white);
  }
  .backdrop {
    position: absolute;
    inset: 0;
    background:
      radial-gradient(ellipse 60% 40% at 70% 30%, rgba(157,157,157,0.28), transparent 70%),
      radial-gradient(ellipse 50% 35% at 20% 55%, rgba(120,120,120,0.22), transparent 70%),
      linear-gradient(180deg, #2a2a2a 0%, #141414 55%, #000 80%);
  }
  .brand {
    position: absolute;
    left: 30px;
    top: 44px;
    display: flex;
    align-items: center;
    gap: 14px;
  }
  .brand-dot {
    width: 22px;
    height: 22px;
    border-radius: 50%;
    background: var(--red);
  }
  .brand-name {
    font-family: "Oswald", sans-serif;
    font-weight: 700;
    font-size: 40px;
    letter-spacing: 1px;
    color: var(--white);
    text-transform: uppercase;
  }
  .photo-frames {
    position: absolute;
    left: 0;
    top: 0;
    width: 849px;
    height: 1200px;
  }
  .headline {
    position: absolute;
    right: 30px;
    top: 712px;
    text-align: right;
    font-family: "Oswald", sans-serif;
    text-transform: uppercase;
    line-height: 1.02;
  }
  .headline-place { font-size: 46px; font-weight: 700; color: var(--red); }
  .headline-title { font-size: 46px; font-weight: 700; color: var(--white); }
  .headline-dates { font-size: 27px; font-weight: 500; color: var(--red); margin-top: 4px; }
  .intro {
    position: absolute;
    left: 30px;
    right: 30px;
    top: 980px;
    font-size: 15px;
    line-height: 1.35;
    color: var(--white);
  }
  .intro p + p { margin-top: 18px; }
</style>
</head>
<body>
<main class="flyer">
  <div class="backdrop" role="img" aria-label="Faded dark photo of a crowd watching a cycling race"></div>

  <header class="brand">
    <span class="brand-dot"></span>
    <span class="brand-name">Bramble Ridge Club</span>
  </header>

  <svg class="photo-frames" viewBox="0 0 849 1200" xmlns="http://www.w3.org/2000/svg">
    <defs>
      <linearGradient id="winner-tones" x1="0" y1="0" x2="1" y2="1">
        <stop offset="0" stop-color="#6f7a86"/>
        <stop offset="0.45" stop-color="#c9ccd2"/>
        <stop offset="0.7" stop-color="#3b5da8"/>
        <stop offset="1" stop-color="#2a2e36"/>
      </linearGradient>
      <linearGradient id="sprint-tones" x1="0" y1="0" x2="0" y2="1">
        <stop offset="0" stop-color="#8a8d92"/>
        <stop offset="0.5" stop-color="#d6d6d6"/>
        <stop offset="1" stop-color="#3a3a3a"/>
      </linearGradient>
    </defs>
    <g role="img" aria-label="Photo of a race winner crossing the finish line with arms raised">
      <polygon points="212,175 770,108 745,560 560,612" fill="url(#winner-tones)"/>
      <polygon points="212,175 770,108 745,560 560,612" fill="none" stroke="var(--red)" stroke-width="9" stroke-linejoin="miter"/>
    </g>
    <g role="img" aria-label="Photo of a cyclist sprinting out of the saddle">
      <polygon points="50,515 330,598 210,860 40,808" fill="url(#sprint-tones)"/>
      <polygon points="50,515 330,598 210,860 40,808" fill="none" stroke="var(--red)" stroke-width="9" stroke-linejoin="miter"/>
    </g>
  </svg>

  <section class="headline">
    <h1 class="headline-place">Tuscany (Italy)</h1>
    <h2 class="headline-title">Training Camps</h2>
    <p class="headline-dates">October and Novembre 2015</p>
  </section>

  <section class="intro">
    <p>At Bramble Ridge Club™, we use cutting edge tools to help talented athletes set and achieve ambitious goals. We don't believe in the status quo. Instead, we think that the next level of performance is a matter of motivation. And if you're willing to do whatever it takes to pursue your goal, you're only one step away from achieving it.</p>
    <p>Bramble Ridge Club™'s unique training program helps high-performance cyclists and competitive athletes assess their current abilities and create a plan to achieve a new level of performance. We use a proprietary combination of Mental Training, Technical Training, and Functional Training to help you break through your personal challenges and reach your full potential.</p>
  </section>
</main>
</body>
</html>
```